Plum & Us Business Card Design

Plum & Us is a company that makes treats and real food for people with food allergies, illnesses and those that like to eat clean. We like to take good old fashioned favorites and create a clean, healthy version of it without losing any of the addictive ‘yumminess’ of it.All of our products are made with Organic ingredients and we aim to be as sustainable as possible therefore I would like this to be reflected in our business cards. I like the thought of using chia seeds in the business card maybe so that people could grow their own.

Industry/Entity Type

Health And Wellness

Contact Information for Business Card

Plum & Uswww.plumandus.com.aumarnie@plumandus.com.auP: 0431 596 218 Facebook and Instagram logos

Requirements
Must have
• Logo - does not have to be the exact logo as long as it is close and fits in with the other information I have asked for (sustainable & Organic, recycled etc.)
• See the photo with the treats for a picture of the logo

```html
<!DOCTYPE html>
<html lang="en">
<head>
<meta charset="utf-8">
<title>Plum &amp; Us — Business Card</title>
<link rel="stylesheet" href="https://fonts.googleapis.com/css2?family=Quicksand:wght@500;600&display=swap">
<style>
  :root {
    --backdrop: #e8e6e1;
    --card: #ffffff;
    --seed-deep: #3c7f25;
    --seed-mid: #5a9f34;
    --seed-light: #8cc44f;
    --ink: #2f2b7c;
    --shadow: rgba(40, 40, 30, 0.22);
  }
  * { box-sizing: border-box; margin: 0; padding: 0; }
  html, body {
    width: 1200px;
    height: 900px;
    overflow: hidden;
    background: var(--backdrop);
    font-family: "Quicksand", sans-serif;
  }
  .business-card {
    position: absolute;
    left: 180px;
    top: 210px;
    width: 840px;
    height: 480px;
    background: var(--card);
    overflow: hidden;
    box-shadow: 0 18px 40px var(--shadow);
  }
  .seed-band {
    position: absolute;
    left: 0;
    right: 0;
  }
  .seed-band--top {
    top: 0;
    height: 150px;
    background: linear-gradient(to bottom,
      var(--seed-deep) 0%,
      var(--seed-mid) 55%,
      rgba(140, 196, 79, 0.55) 80%,
      rgba(255, 255, 255, 0) 100%);
  }
  .seed-band--bottom {
    bottom: 0;
    height: 175px;
    background: linear-gradient(to top,
      var(--seed-deep) 0%,
      var(--seed-mid) 55%,
      rgba(140, 196, 79, 0.55) 80%,
      rgba(255, 255, 255, 0) 100%);
  }
  .card-content {
    position: absolute;
    left: 0;
    right: 0;
    top: 128px;
    text-align: center;
    color: var(--ink);
  }
  .brand-name {
    font-size: 66px;
    font-weight: 600;
    line-height: 1;
    letter-spacing: 1px;
    color: var(--ink);
    margin-bottom: 26px;
  }
  .contact-list {
    list-style: none;
    font-size: 22px;
    font-weight: 500;
    line-height: 32px;
    letter-spacing: 0.5px;
  }
  .contact-phone {
    display: inline-flex;
    align-items: center;
    gap: 10px;
  }
  .phone-icon {
    width: 13px;
    height: 20px;
  }
</style>
</head>
<body>
  <main class="business-card">
    <div class="seed-band seed-band--top" role="img" aria-label="Photograph of green chia seeds"></div>
    <div class="seed-band seed-band--bottom" role="img" aria-label="Photograph of green chia seeds"></div>

    <section class="card-content">
      <h1 class="brand-name">Plum &amp; Us</h1>
      <ul class="contact-list">
        <li class="contact-phone">
          <svg class="phone-icon" viewBox="0 0 13 20" aria-hidden="true">
            <rect x="1" y="1" width="11" height="18" rx="2" fill="none" stroke="#2f2b7c" stroke-width="1.8"/>
            <line x1="5" y1="16" x2="8" y2="16" stroke="#2f2b7c" stroke-width="1.5"/>
          </svg>
          <span>0431 596 218</span>
        </li>
        <li class="contact-web">www.plumandus.com.au</li>
        <li class="contact-email">marnie@plumandus.com.au</li>
      </ul>
    </section>
  </main>
</body>
</html>
```